I am a surgeon that operates on gynaecological cancer. Wish a design and logo for letter head.

Design should include my name: Dr. Kiran Mudaly, qualifications: FTELSWOB, CGO. and state that I am a Gynaecological Oncologist and Advanced Laparoscopic Surgeon.
As for a logo. As all cancer is related to DNA, I think that that double helix could be used to symbolise a female shape, exaggerating the abdomen to suggest a mass.

Reason: Extended to view changes I have asked for.

```html
<!DOCTYPE html>
<html lang="en">
<head>
<meta charset="utf-8">
<title>Dr. Kiran Mudaly – Stationery</title>
<link rel="stylesheet" href="https://fonts.googleapis.com/css2?family=Questrial&family=Tinos&display=swap">
<style>
  :root {
    --backdrop: #f1f2f2;
    --paper: #ffffff;
    --edge: #e2e4e4;
    --teal: #1aa39a;
    --green: #8cc63f;
    --label-grey: #b3b3b3;
    --faint-teal: #d5eeec;
    --faint-green: #e6f3d6;
  }
  * { margin: 0; padding: 0; box-sizing: border-box; }
  html, body {
    width: 1200px; height: 1200px; overflow: hidden;
    background: var(--backdrop);
    font-family: "Questrial", "Century Gothic", sans-serif;
  }
  .canvas { position: relative; width: 1200px; height: 1200px; }

  .letterhead {
    position: absolute; left: 74px; top: 81px;
    width: 756px; height: 1019px;
    background: var(--paper);
    border: 1px solid var(--edge);
  }
  .letterhead-decor { position: absolute; inset: 0; }

  .business-card {
    position: absolute; left: 604px; top: 465px;
    width: 512px; height: 255px;
    background: var(--paper);
    border: 1px solid var(--edge);
  }
  .card-label {
    position: absolute; left: 10px; top: 10px;
    font-family: "Tinos", "Times New Roman", serif;
    font-size: 22px; color: var(--label-grey);
  }

  .lockup {
    position: absolute; left: 0; right: 0;
    display: flex; flex-direction: column; align-items: center;
  }
  .lockup-mark { border-radius: 50%; background: var(--teal); }
  .lockup-title { color: var(--teal); line-height: 1; }
  .lockup-name { color: var(--teal); letter-spacing: 0.12em; line-height: 1; }
  .lockup-credentials {
    display: flex; align-items: center; color: var(--green); line-height: 1;
  }
  .lockup-credentials::before,
  .lockup-credentials::after {
    content: ""; display: block; height: 2px; background: var(--green);
  }

  .letterhead .lockup { top: 18px; }
  .letterhead .lockup-mark { width: 60px; height: 60px; margin-bottom: 20px; }
  .letterhead .lockup-title { font-size: 9px; margin-bottom: 2px; }
  .letterhead .lockup-name { font-size: 21px; }
  .letterhead .lockup-credentials { font-size: 10px; margin-top: 3px; gap: 6px; }
  .letterhead .lockup-credentials::before,
  .letterhead .lockup-credentials::after { width: 48px; height: 1.5px; }

  .business-card .lockup { top: 38px; }
  .business-card .lockup-mark { width: 96px; height: 96px; margin-bottom: 36px; }
  .business-card .lockup-title { font-size: 13px; margin-bottom: 2px; }
  .business-card .lockup-name { font-size: 32px; }
  .business-card .lockup-credentials { font-size: 15px; margin-top: 5px; gap: 10px; }
  .business-card .lockup-credentials::before,
  .business-card .lockup-credentials::after { width: 66px; }
</style>
</head>
<body>
<main class="canvas">

  <section class="letterhead" aria-label="Letterhead">
    <svg class="letterhead-decor" width="756" height="1019" viewBox="0 0 756 1019" aria-hidden="true">
      <g fill="var(--faint-teal)">
        <circle cx="524" cy="706" r="26"/>
        <circle cx="679" cy="675" r="18"/>
        <circle cx="621" cy="810" r="34"/>
        <circle cx="377" cy="871" r="26"/>
        <circle cx="505" cy="946" r="23"/>
        <circle cx="665" cy="974" r="20"/>
        <circle cx="160" cy="940" r="18"/>
        <circle cx="271" cy="981" r="18"/>
        <circle cx="58" cy="977" r="20"/>
      </g>
    </svg>
    <div class="lockup">
      <div class="lockup-mark" aria-hidden="true"></div>
      <span class="lockup-title">DR.</span>
      <h1 class="lockup-name">KIRAN MUDALY</h1>
      <p class="lockup-credentials">FTELSWOB, CGO.</p>
    </div>
  </section>

  <section class="business-card" aria-label="Business card">
    <span class="card-label">LOGO</span>
    <div class="lockup">
      <div class="lockup-mark" aria-hidden="true"></div>
      <span class="lockup-title">DR.</span>
      <h2 class="lockup-name">KIRAN MUDALY</h2>
      <p class="lockup-credentials">FTELSWOB, CGO.</p>
    </div>
  </section>

</main>
</body>
</html>
```